Quarveling stickers design for our main topics (for example: agile and Kanban)

We are looking for sticker design, that will reflect our cooperate identity and can be used for the different topics in our company. We would like to start with our Agile Coaching Offers with a Kanban Sticker saying "stop starting, start finishing", A bad example can be find in the file upload ;)
Check out our homepage to get a feeling for the cooperate identity (www.quarveling.ch)

Target Market(s)

Customers and trainees from our trainings

Industry/Entity Type

Consulting

Colors
0355a3
fbed22

Requirements
Must have
• a cool design thats fits to our customer design
the 2 lines can be changed for future stickers ... like in the example "stop starting, start finishing" and "we show you how"
Nice to have
• -
Should not have
• -

```html
<!DOCTYPE html>
<html lang="en">
<head>
<meta charset="utf-8">
<title>Quarveling Sticker – Stop Starting, Start Finishing</title>
<link rel="stylesheet" href="https://fonts.googleapis.com/css2?family=Poppins:wght@600&family=Arimo:wght@400&display=swap">
<style>
  :root {
    --frame-blue: #2f5597;
    --brand-blue: #0355a3;
    --brand-yellow: #fbed22;
    --ink: #000000;
    --paper: #ffffff;
    --hand-tint: #dde7f4;
  }
  html, body {
    margin: 0;
    padding: 0;
    background: var(--paper);
    overflow: hidden;
  }
  .sticker {
    width: 1200px;
    height: 686px;
    position: relative;
    overflow: hidden;
    background: var(--paper);
  }
  .sticker__art {
    display: block;
    width: 1200px;
    height: 686px;
  }
  .sticker__frame {
    fill: none;
    stroke: var(--frame-blue);
    stroke-width: 3.2;
  }
  .stop-badge {
    fill: none;
    stroke: var(--brand-yellow);
    stroke-width: 9.5;
  }
  .play-badge {
    fill: none;
    stroke: var(--brand-blue);
    stroke-width: 9;
    stroke-linejoin: round;
  }
  .headline {
    font-family: "Poppins", sans-serif;
    font-weight: 600;
    fill: var(--ink);
  }
  .badge-label {
    font-family: "Poppins", sans-serif;
    font-weight: 600;
    fill: var(--ink);
  }
  .tagline {
    font-family: "Arimo", sans-serif;
    font-weight: 400;
    fill: var(--ink);
  }
  .hand-illustration {
    fill: var(--hand-tint);
  }
  .brand-mark {
    fill: var(--brand-blue);
  }
  .brand-name {
    font-family: "Arimo", sans-serif;
    font-weight: 400;
    fill: var(--ink);
  }
</style>
</head>
<body>
  <main class="sticker">
    <svg class="sticker__art" viewBox="0 0 1200 686" xmlns="http://www.w3.org/2000/svg">
      <!-- outer sticker outline -->
      <rect class="sticker__frame" x="25" y="177" width="1114" height="350" rx="54" ry="54"/>

      <!-- line one: stop starting -->
      <g class="line line--stop">
        <rect class="stop-badge" x="176" y="240.5" width="76" height="76" rx="11" ry="11"/>
        <text class="badge-label" x="183" y="309.5" font-size="26" textLength="63" lengthAdjust="spacingAndGlyphs">STOP</text>
        <text class="headline" x="267" y="305.5" font-size="76" textLength="342" lengthAdjust="spacingAndGlyphs">STARTING</text>
      </g>

      <!-- line two: start finishing -->
      <g class="line line--start">
        <text class="badge-label" transform="translate(345.5 408) rotate(-90)" font-size="27" textLength="74" lengthAdjust="spacingAndGlyphs">START</text>
        <path class="play-badge" d="M361 338 Q357 336 357 341 L357 400 Q357 406 362 403 L418 373 Q424 370 418 366 Z"/>
        <text class="headline" x="437" y="394" font-size="75" textLength="337" lengthAdjust="spacingAndGlyphs">FINISHING</text>
      </g>

      <!-- tagline -->
      <g class="line line--tagline">
        <text class="tagline" x="581" y="471.5" font-size="42" textLength="181" lengthAdjust="spacingAndGlyphs">We Show</text>
        <rect class="hand-illustration" x="777" y="428" width="71" height="67" rx="14" ry="14" role="img" aria-label="Illustration of a blue outlined hand pointing at the viewer"/>
        <text class="tagline" x="859" y="471.5" font-size="42" textLength="82" lengthAdjust="spacingAndGlyphs">How</text>
      </g>

      <!-- company name -->
      <g class="brand">
        <rect class="brand-mark" x="982" y="451" width="20" height="20"/>
        <text class="brand-name" x="1008" y="454" font-size="16" textLength="84" lengthAdjust="spacingAndGlyphs">quarveling ag</text>
      </g>
    </svg>
  </main>
</body>
</html>
```